Brindle's Business Card

I need some designs for a new business card including the new logo attached. An old example of our business card is also attached to show all the data that should be included on the new design.
**I added some more examples someone had mocked up**

Contact Information for Business Card

Should include all info on other examples uploaded.

```html
<!DOCTYPE html>
<html lang="en">
<head>
<meta charset="utf-8">
<title>Brindle's Business Card</title>
<link href="https://fonts.googleapis.com/css2?family=Roboto+Condensed:wght@300;400;700&display=swap" rel="stylesheet">
<style>
  :root {
    --page: #d9d9d9;
    --card-white: #ffffff;
    --brand-blue: #1a6fc4;
    --brand-red: #e3262f;
    --back-blue: #0a76cc;
    --back-blue-light: #3b91dc;
  }
  * { box-sizing: border-box; margin: 0; padding: 0; }
  html, body { width: 1200px; height: 846px; overflow: hidden; }
  body {
    background: var(--page);
    font-family: "Roboto Condensed", "Arial Narrow", sans-serif;
    position: relative;
  }
  .card {
    position: absolute;
    top: 268px;
    width: 540px;
    height: 309px;
    box-shadow: 0 6px 18px rgba(0,0,0,0.18);
  }
  .card-front { left: 40px; background: var(--card-white); }
  .card-back {
    left: 620px;
    background: linear-gradient(135deg, var(--back-blue-light) 0%, var(--back-blue) 55%, var(--back-blue) 100%);
  }

  .brand {
    position: absolute;
    left: 38px;
    top: 92px;
    width: 150px;
    display: flex;
    align-items: center;
    gap: 8px;
  }
  .brand-dot {
    width: 16px; height: 16px; border-radius: 50%;
    background: var(--brand-red);
    flex: none;
  }
  .brand-name {
    font-weight: 700;
    font-size: 30px;
    color: var(--brand-blue);
    letter-spacing: 0.5px;
  }

  .divider {
    position: absolute;
    left: 205px; top: 52px;
    width: 1px; height: 118px;
    background: var(--brand-blue);
  }

  .contact {
    position: absolute;
    left: 226px; top: 52px;
    color: var(--brand-blue);
  }
  .person-name { font-size: 26px; font-weight: 700; line-height: 1.05; }
  .person-name .surname { color: var(--brand-red); }
  .credential { font-size: 17px; font-weight: 300; margin-bottom: 8px; }
  .contact-row {
    display: flex; align-items: center; gap: 10px;
    font-size: 20px; font-weight: 400; line-height: 1.45;
  }
  .contact-row svg { width: 20px; height: 20px; flex: none; }

  .services {
    position: absolute;
    left: 0; right: 0; top: 206px;
    text-align: center;
  }
  .services-line {
    font-size: 17px; font-weight: 400; color: var(--brand-blue);
    text-transform: uppercase; letter-spacing: 0.2px;
  }
  .area-line {
    display: flex; align-items: center; justify-content: center; gap: 12px;
    margin-top: 2px;
    font-size: 17px; color: var(--brand-red); text-transform: uppercase;
  }
  .area-line::before, .area-line::after {
    content: ""; width: 58px; height: 1px; background: var(--brand-red);
  }
</style>
</head>
<body>
  <section class="card card-front">
    <div class="brand">
      <span class="brand-dot"></span>
      <span class="brand-name">Brindle's</span>
    </div>
    <div class="divider"></div>
    <div class="contact">
      <p class="person-name">Wade <span class="surname">Brindle</span></p>
      <p class="credential">Licensed &amp; Insured</p>
      <p class="contact-row">
        <svg viewBox="0 0 24 24" aria-hidden="true"><path fill="#e3262f" d="M6.6 10.8a15.1 15.1 0 0 0 6.6 6.6l2.2-2.2a1 1 0 0 1 1-.25 11.4 11.4 0 0 0 3.6.57 1 1 0 0 1 1 1V20a1 1 0 0 1-1 1A17 17 0 0 1 3 4a1 1 0 0 1 1-1h3.5a1 1 0 0 1 1 1c0 1.25.2 2.45.57 3.57a1 1 0 0 1-.25 1z"/></svg>
        555 014 2287
      </p>
      <p class="contact-row">
        <svg viewBox="0 0 24 24" aria-hidden="true"><rect x="2" y="5" width="20" height="14" rx="2" fill="#e3262f"/><path d="M3 6l9 7 9-7" fill="none" stroke="#fff" stroke-width="1.6"/></svg>
        hvacbrindle@example.com
      </p>
    </div>
    <div class="services">
      <p class="services-line">Call today for all your HVAC, refrigeration &amp; plumbing needs</p>
      <p class="area-line">Serves Maple Ridge, IA &amp; surrounding areas</p>
    </div>
  </section>

  <section class="card card-back" role="img" aria-label="Repeating pattern of the Brindle's name in soft blue tones across the card back"></section>
</body>
</html>
```